Ashgrove Timberworks highend custom homes

We build high end custom homes and timber frames we specialize in rustic hand made designs along with iron and concrete accents to add a modern touch 90% of my homes are buit on lake front properries attached is my logo and slogan as of now and my previous one

Target Market(s)

High end custom homes

Industry/Entity Type

Custom residential construction

Contact Information for Business Card

Been in buissness 8+ years inssured and reliable

Colors
A7469A
B969AE
D3A5CF
EDDBEB
F8F0F9

Requirements
Must have
• Must have slogan and phone number
Should not have
• A combination of rustic yet modern accents

```html
<!DOCTYPE html>
<html lang="en">
<head>
<meta charset="UTF-8">
<title>Ashgrove Timberworks – Business Card</title>
<link rel="stylesheet" href="https://fonts.googleapis.com/css2?family=Jost:wght@400;700&family=Lato:wght@400&family=Arimo:wght@400&display=swap">
<style>
  :root {
    --backdrop: #1b1b1b;
    --kraft-light: #dfbd91;
    --kraft-mid: #c79d6a;
    --kraft-dark: #a6784a;
    --forest: #4d5c48;
    --ink: #2b2a26;
    --ink-soft: #46443d;
  }
  * { margin: 0; padding: 0; box-sizing: border-box; }
  html, body {
    width: 1093px;
    height: 1200px;
    overflow: hidden;
    background: var(--backdrop);
  }
  .canvas {
    position: relative;
    width: 1093px;
    height: 1200px;
  }
  .card {
    position: absolute;
    left: 264px;
    width: 580px;
    height: 357px;
    background: linear-gradient(135deg, var(--kraft-light) 0%, var(--kraft-mid) 55%, var(--kraft-dark) 100%);
    text-align: center;
  }
  .card--contact { top: 226px; }
  .card--brand { top: 620px; }

  .contact__name {
    position: absolute;
    top: 68px;
    width: 100%;
    font-family: 'Jost', sans-serif;
    font-weight: 700;
    font-size: 21px;
    line-height: 24px;
    letter-spacing: 0.3px;
    color: var(--forest);
  }
  .contact__role {
    position: absolute;
    top: 92px;
    width: 100%;
    font-family: 'Arimo', Arial, sans-serif;
    font-size: 15.5px;
    line-height: 18px;
    color: var(--ink);
  }
  .divider {
    position: absolute;
    left: 50%;
    width: 94px;
    margin-left: -47px;
    height: 1px;
    background: var(--ink);
  }
  .divider--top { top: 124px; }
  .divider--bottom { top: 223px; }
  .contact__details, .contact__address {
    position: absolute;
    width: 100%;
    font-family: 'Lato', sans-serif;
    font-size: 16.5px;
    line-height: 21px;
    color: var(--ink);
    list-style: none;
  }
  .contact__details { top: 142px; }
  .contact__address { top: 240px; font-style: normal; }

  .brand__lockup {
    position: absolute;
    top: 128px;
    width: 100%;
    display: flex;
    align-items: center;
    justify-content: center;
    gap: 12px;
  }
  .brand__square {
    width: 22px;
    height: 22px;
    background: var(--forest);
  }
  .brand__name {
    font-family: 'Jost', sans-serif;
    font-weight: 700;
    font-size: 32px;
    line-height: 40px;
    letter-spacing: 0.5px;
    color: var(--forest);
    text-transform: uppercase;
  }
  .brand__slogan {
    position: absolute;
    top: 178px;
    width: 100%;
    display: flex;
    align-items: center;
    justify-content: center;
    gap: 8px;
    font-family: 'Jost', sans-serif;
    font-weight: 400;
    font-size: 15px;
    letter-spacing: 0.4px;
    color: var(--ink-soft);
    text-transform: uppercase;
  }
  .brand__dot {
    width: 5px;
    height: 5px;
    border-radius: 50%;
    background: var(--ink);
  }
</style>
</head>
<body>
<main class="canvas">
  <section class="card card--contact">
    <h1 class="contact__name">DANIEL HARLOW</h1>
    <p class="contact__role">Managing Director</p>
    <div class="divider divider--top"></div>
    <ul class="contact__details">
      <li>M: 044-555 218 904</li>
      <li>E: hello@ashgrovetimber.com</li>
      <li>W: www.ashgrovetimber.com</li>
    </ul>
    <div class="divider divider--bottom"></div>
    <address class="contact__address">
      12345, Address Goes Here<br>
      Country Name, 123456.
    </address>
  </section>

  <section class="card card--brand">
    <div class="brand__lockup">
      <span class="brand__square"></span>
      <span class="brand__name">Ashgrove Timberworks</span>
    </div>
    <p class="brand__slogan">
      <span class="brand__dot"></span>
      From Lodges to Lakehouses
      <span class="brand__dot"></span>
    </p>
  </section>
</main>
</body>
</html>
```